sailbrightly Website for children with diabilities

Hi, we are looking for a new website design for our community service "sailbrightly". Sailbrightly gives children who suffer from diseases or disabilities a week off on a Boat to give the children new hope and an unforgettable experience.

The current website is really old and we want to have a new one.
Please feel free to discover our website under http://sailbrightly-example.at/.
We have several company sponsors which are very important to us.

The Website has to be a Bootstrap Design (Version 4.4 or higher) [NOT Wordpress, Joomla, other CMS]

Target Market(s)

no target market. we like to inform our communities about our service.

Industry/Entity Type

community service for children with disabilities

Coding

Number of Pages Required

4 page

Font styles to use
Sans Serif

Colors
0054AA
0677BA
7BADD7
CADEEF
E8F1F8
0094D4
00A9DD
6FCCEA
C7EBF8
E9F6FB

Requirements
Must have
• About, Sponsors, Information about cruises
Nice to have
• Gallery

```html
<!DOCTYPE html>
<html lang="de">
<head>
<meta charset="utf-8">
<title>Verein Sailbrightly</title>
<link href="https://fonts.googleapis.com/css2?family=Nunito:wght@400;600;700;800&family=Amaranth:wght@700&display=swap" rel="stylesheet">
<style>
:root{
  --blue-deep:#0054AA;
  --blue:#0677BA;
  --blue-mid:#7BADD7;
  --blue-pale:#CADEEF;
  --bg:#E8F1F8;
  --sky:#0094D4;
  --sky-bright:#00A9DD;
  --sky-soft:#6FCCEA;
  --navy:#1b2a6b;
  --text:#2b2f3a;
  --white:#ffffff;
}
*{margin:0;padding:0;box-sizing:border-box}
html,body{width:1200px;height:4261px;overflow:hidden}
body{font-family:"Nunito",sans-serif;background:var(--bg);color:var(--text)}
.page{position:relative;width:1200px;height:4261px;overflow:hidden;background:var(--bg)}
.abs{position:absolute}

/* top bar */
.topbar{left:0;top:0;width:1200px;height:28px;background:var(--blue-deep);color:var(--white);font-size:11px}
.topbar .social{position:absolute;left:160px;top:9px;display:flex;gap:12px}
.dot{display:block;width:9px;height:9px;border-radius:50%;background:var(--white)}
.topbar .reg{position:absolute;right:164px;top:7px}

/* header */
.header{left:0;top:28px;width:1200px;height:111px;background:var(--white)}
.brand{display:flex;align-items:center;gap:10px;color:var(--navy);font-weight:800;font-size:22px;line-height:23px}
.brand .mark{width:70px;height:70px;border-radius:50%;background:var(--navy)}
.header .brand{position:absolute;left:160px;top:20px}
.nav{display:flex;gap:52px;font-size:13px;font-weight:600;color:var(--navy);letter-spacing:.3px}
.header .nav{position:absolute;right:164px;top:48px}

/* hero */
.hero{left:0;top:139px;width:1200px;height:560px}
.hero-quote{left:652px;top:146px;width:420px;color:var(--white)}
.hero-quote h1{font-family:"Amaranth",sans-serif;font-size:30px;line-height:37px;font-weight:700}
.hero-quote p{font-size:25px;margin-top:12px;font-weight:400}

/* sections */
.section-title{color:var(--blue-deep);font-weight:800;font-size:29px;line-height:36px}
.body-copy{font-size:12.6px;line-height:24.4px;color:var(--text)}
.photo{border-radius:50%;border:3px solid var(--blue)}
.splash{border-radius:50%;background:radial-gradient(circle,rgba(123,173,215,.75) 45%,rgba(202,222,239,.35) 62%,rgba(232,241,248,0) 72%)}
.centered{text-align:center;width:1200px;left:0}

/* goals */
.goal-label{font-size:15px;font-weight:700;line-height:24px;color:var(--text)}

/* gallery */
.tile{border-radius:0}

/* footer */
.footer{left:0;top:3964px;width:1200px;height:297px}
.footer .brand{position:absolute;left:497px;top:80px;color:var(--white)}
.footer .brand .mark{background:var(--navy);width:72px;height:72px}
.footer .nav{position:absolute;left:0;width:1200px;top:183px;justify-content:center;color:var(--white)}
.footer .rule{position:absolute;left:160px;width:880px;top:224px;height:1px;background:rgba(255,255,255,.3)}
.footer .copy{position:absolute;left:160px;top:265px;color:var(--white);font-size:12.5px}
.footer .social{position:absolute;right:164px;top:268px;display:flex;gap:22px}
.footer .dot{width:11px;height:11px}
</style>
</head>
<body>
<div class="page">

  <div class="abs topbar">
    <div class="social" aria-label="Soziale Netzwerke"><span class="dot"></span><span class="dot"></span><span class="dot"></span><span class="dot"></span></div>
    <div class="reg">Eingetragener Verein ZVR-Zahl: 012345678</div>
  </div>

  <header class="abs header">
    <div class="brand"><span class="mark"></span><span>Verein<br>Sailbrightly</span></div>
    <nav class="nav"><span>HEIM</span><span>UM</span><span>SPONSOR</span><span>INFORMATIONEN ÜBER KREUZFAHRT</span></nav>
  </header>

  <svg class="abs hero" viewBox="0 0 1200 560" role="img" aria-label="Kinder auf einem Segelboot am Steg, dahinter Wasser und Bäume">
    <defs>
      <linearGradient id="heroFill" x1="0" y1="0" x2="1" y2="0">
        <stop offset="0" stop-color="#2a8fd0"/>
        <stop offset=".45" stop-color="#5f8fa8"/>
        <stop offset=".7" stop-color="#3f6f97"/>
        <stop offset="1" stop-color="#2b5b8e"/>
      </linearGradient>
    </defs>
    <path d="M0 0H1200V420Q900 540 600 548Q300 540 0 420Z" fill="#1d2d75"/>
    <path d="M0 0H1200V405Q900 525 600 534Q300 525 0 405Z" fill="url(#heroFill)"/>
    <circle cx="600" cy="531" r="17" fill="#1d2d75"/>
    <path d="M600 522V540M594 534L600 540L606 534" stroke="#fff" stroke-width="1.6" fill="none"/>
  </svg>
  <div class="abs hero-quote">
    <h1>Wir Können Die Windrichtung Nicht Bestimmen, Aber Wir Können Die Segel Richtig Setzen!</h1>
    <p>Marius Velten Aurel</p>
  </div>

  <!-- Wir Sind -->
  <div class="abs splash" style="left:612px;top:712px;width:480px;height:480px"></div>
  <div class="abs photo" role="img" aria-label="Zwei lachende Freiwillige in türkisen T-Shirts" style="left:673px;top:773px;width:358px;height:358px;background:linear-gradient(160deg,#b9d8ef,#27b6d8 55%,#4c7a3c)"></div>
  <h2 class="abs section-title" style="left:160px;top:871px">Wir Sind</h2>
  <p class="abs body-copy" style="left:160px;top:914px;width:430px">Ausgebildete SozialpädagogInnen und erfahrene SkipperInnen, die sich ehrenamtlich im Verein Sailbrightly engagieren und alljährlich für sozial benachteiligte Kinder und Jugendliche, aus dem oberösterreichischen Zentralraum, eine Flotte organisieren und die dafür notwendigen finanziellen Mittel aufstellen.</p>

  <!-- Wir Wollen -->
  <div class="abs splash" style="left:108px;top:1155px;width:480px;height:480px"></div>
  <div class="abs photo" role="img" aria-label="Vater trägt Kind huckepack am Strand" style="left:169px;top:1216px;width:358px;height:358px;background:linear-gradient(170deg,#8aa6b4,#d8c6aa 55%,#b49574)"></div>
  <h2 class="abs section-title" style="left:588px;top:1265px">Wir Wollen</h2>
  <p class="abs body-copy" style="left:588px;top:1308px;width:455px">Kindern und Jugendlichen, die es im Leben nicht immer leicht haben, eine unvergessliche Woche in Kroatien ermöglichen. Denn genau dieses gemeinsame Erlebnis vermittelt den Kindern und Jugendlichen neue Lebensfreude und Perspektiven für ihre Zukunft.  Durch die Reflexion und auch die Betreuung danach in den einzelnen Einrichtungen, können die Kinder und Jugendlichen noch lange an diesem Erlebnis zehren. Diese Nachhaltigkeit schafft zahlreiche pädagogische Anknüpfungspunkte, die für die Zielerreichung eine wertvolle Grundlage darstellen.</p>

  <!-- Praktische Umsetzung -->
  <div class="abs splash" style="left:612px;top:1600px;width:480px;height:480px"></div>
  <div class="abs photo" role="img" aria-label="Mädchen mit Mütze steuert ein Segelboot" style="left:673px;top:1661px;width:358px;height:358px;background:linear-gradient(150deg,#3c6fa0,#e9e4dc 50%,#7a5a44)"></div>
  <h2 class="abs section-title" style="left:160px;top:1657px">Praktische Umsetzung der<br>pädagogischen Überlegungen</h2>
  <p class="abs body-copy" style="left:160px;top:1748px;width:440px">Die TeilnehmerInnen werden bewusst zu Tätigkeiten beim Segeln herangezogen. Es gibt Verantwortlichkeiten für verschiedenste Aufgaben im täglichen Zusammenleben. Ein Koch- und Putzplan soll dazu beitragen, Verantwortung gegenüber der Gruppe zu übernehmen. Die Tatsache, ein Segelschiff alleine zu steuern, erfüllt so manchen mit großem Stolz. Wiederkehrende Tätigkeiten am Schiff erfordern die Beteiligung jedes Crewmitglieds. So wird allen das Gefühl vermittelt, eine Bedeutung für die Gemeinschaft zu haben und jede/r lernt dabei, diese Verantwortung nach eigener Möglichkeit auch zu tragen. Sailbrightly bietet ein ideales Übungsfeld für soziales Lernen. Die intensive Auseinandersetzung mit anderen und der Gruppe auf engstem Raum, bietet verschiedenste Möglichkeiten, sich im Umgang mit Mitmenschen zu erproben. All diese Erfahrungen können zu einer Aufwertung ihrer selbst führen.</p>

  <!-- Projektziele -->
  <h2 class="abs section-title centered" style="top:2193px">Projektziele</h2>
  <svg class="abs" style="left:0;top:2250px" width="1200" height="470" viewBox="0 0 1200 470" aria-label="Projektziele Übersicht">
    <circle cx="599" cy="100" r="58" fill="var(--blue-deep)"/>
    <path d="M473 100A126 126 0 0 0 725 100" fill="none" stroke="#7BADD7" stroke-width="2"/>
    <path d="M540 210A126 126 0 0 0 658 210" fill="none" stroke="#0094D4" stroke-width="6" stroke-linecap="round"/>
    <g fill="#fff" stroke="#7BADD7" stroke-width="1.5">
      <circle cx="473" cy="100" r="4"/><circle cx="725" cy="100" r="4"/>
      <circle cx="493" cy="168" r="4"/><circle cx="705" cy="168" r="4"/>
      <circle cx="560" cy="218" r="4"/><circle cx="638" cy="218" r="4"/>
    </g>
    <g fill="#fff">
      <path d="M300 110H420Q440 110 445 130L455 215Q450 245 420 255L360 278Q330 280 318 255L298 130Q296 110 300 110Z"/>
      <path d="M385 240L470 195Q490 188 505 200L530 260Q535 280 520 295L455 330Q430 340 415 320L380 270Q372 250 385 240Z"/>
      <path d="M520 300L678 300Q690 300 688 315L680 405Q678 420 663 420H535Q520 420 518 405L510 315Q510 300 520 300Z"/>
      <path d="M815 240L730 195Q710 188 695 200L670 260Q665 280 680 295L745 330Q770 340 785 320L820 270Q828 250 815 240Z"/>
      <path d="M900 110H780Q760 110 755 130L745 215Q750 245 780 255L840 278Q870 280 882 255L902 130Q904 110 900 110Z"/>
    </g>
    <g fill="none" stroke="var(--blue-deep)" stroke-width="2.4" stroke-linecap="round" stroke-linejoin="round">
      <circle cx="370" cy="175" r="20"/><path d="M362 180Q370 188 378 180M360 150L356 142M370 148V139M380 150L384 142"/>
      <circle cx="423" cy="270" r="8"/><circle cx="463" cy="270" r="8"/><path d="M410 305V285H436V305M450 305V285H476V305M430 248H458M452 243L458 248L452 253"/>
      <circle cx="580" cy="345" r="8"/><path d="M568 395V360H592V395M562 368L598 368"/><ellipse cx="620" cy="355" rx="18" ry="25"/>
      <path d="M735 270Q760 255 780 268M725 300H770Q790 300 790 285"/><circle cx="750" cy="285" r="6"/><circle cx="765" cy="285" r="6"/>
      <rect x="800" cy="0" y="152" width="50" height="50" rx="12"/><circle cx="825" cy="177" r="12"/>
    </g>
  </svg>
  <p class="abs goal-label" style="left:93px;top:2416px;width:200px;text-align:right">Erlebnisorientiertes<br>Lernen</p>
  <p class="abs goal-label" style="left:112px;top:2583px;width:280px;text-align:right">Erarbeiten gewaltfreier<br>Konfliktlösungsstrategien</p>
  <p class="abs goal-label" style="left:400px;top:2666px;width:400px;text-align:center">Stärkung des Selbstwertgefühls<br>und der sozialen Kompetenz</p>
  <p class="abs goal-label" style="left:798px;top:2583px;width:260px">Verantwortung für sich selbst<br>und andere übernehmen</p>
  <p class="abs goal-label" style="left:912px;top:2416px;width:160px">Üben von<br>Toleranz</p>

  <!-- Erreichte Ziele -->
  <div class="abs splash" style="left:108px;top:2739px;width:480px;height:480px"></div>
  <div class="abs photo" role="img" aria-label="Viele Hände übereinander gelegt" style="left:169px;top:2800px;width:358px;height:358px;background:linear-gradient(150deg,#5a4030,#b88a6a 50%,#2e2620)"></div>
  <h2 class="abs section-title" style="left:588px;top:2885px">Erreichte Ziele</h2>
  <p class="abs body-copy" style="left:588px;top:2928px;width:430px">Durch das Erlebnis einer gemeinsamen Segelwoche schafft die "Sailbrightly Flotte" ideale Bedingungen, unter denen die Leitziele wie soziale Integration und pädagogische Weiterentwicklung der Kinder auf konkrete, effiziente und professionelle Weise, und mit nachhaltiger Wirkung umgesetzt wurden.</p>

  <!-- Galerie -->
  <h2 class="abs section-title centered" style="top:3242px">UnsereGalerie</h2>
  <div class="abs tile" role="img" aria-label="Kinder malen gemeinsam am Tisch" style="left:160px;top:3312px;width:277px;height:354px;background:linear-gradient(160deg,#e8dfd4,#9a6b4f 60%,#5b3a6e)"></div>
  <div class="abs tile" role="img" aria-label="Kinder zeichnen am Tisch mit Buntstiften" style="left:160px;top:3688px;width:277px;height:195px;background:linear-gradient(160deg,#d9d4cc,#eae6e0 55%,#b7a691)"></div>
  <div class="abs tile" role="img" aria-label="Kinder auf einem Segelboot am Meer" style="left:462px;top:3312px;width:276px;height:275px;background:linear-gradient(170deg,#9cc2d8,#d9dfe2 50%,#3f86a8)"></div>
  <div class="abs tile" role="img" aria-label="Betreuerin malt mit einem Kind" style="left:462px;top:3610px;width:276px;height:273px;background:linear-gradient(160deg,#f1dfc8,#c5663f 55%,#e9e2da)"></div>
  <div class="abs tile" role="img" aria-label="Kinder mit Schwimmwesten auf einem Boot" style="left:763px;top:3312px;width:277px;height:275px;background:linear-gradient(180deg,#4f9de0,#c9e3f6 55%,#e7dbc2)"></div>
  <div class="abs tile" role="img" aria-label="Mädchen im Rollstuhl mit Basketball" style="left:763px;top:3610px;width:277px;height:273px;background:linear-gradient(160deg,#6f8f4a,#c77a3a 50%,#3c6d9a)"></div>

  <!-- Footer -->
  <footer class="abs footer">
    <svg class="abs" style="left:0;top:0" width="1200" height="297" viewBox="0 0 1200 297" aria-hidden="true">
      <defs><linearGradient id="foot" x1="0" y1="0" x2="0" y2="1"><stop offset="0" stop-color="#6FCCEA"/><stop offset=".25" stop-color="#0094D4"/><stop offset="1" stop-color="#0054AA"/></linearGradient></defs>
      <path d="M0 14Q100 4 200 12T400 10T600 14T800 8T1000 13T1200 10V297H0Z" fill="url(#foot)"/>
    </svg>
    <div class="brand"><span class="mark"></span><span>Verein<br>Sailbrightly</span></div>
    <nav class="nav"><span>HEIM</span><span>UM</span><span>SPONSOR</span><span>INFORMATIONEN ÜBER KREUZFAHRT</span></nav>
    <div class="rule"></div>
    <p class="copy">© 2022 Verein Sailbrightly. Alle Rechte vorbehalten.</p>
    <div class="social" aria-label="Soziale Netzwerke"><span class="dot"></span><span class="dot"></span><span class="dot"></span><span class="dot"></span></div>
  </footer>
</div>
</body>
</html>
```